Business card required for IT Consultancy Business - Tealbrook Consulting.
Company provides the whole nine yards of services across IT Architecture, design and execution.
Basically we provide consulting services to help businesses make sure their technology is enabling their business strategy.
Design for front and back required.
We would like the front of the card to inlcude:
Name
Title
Mobile number
email address
www.tbkc.com.au
Company logos attached.
Thank you
Industry/Entity Type
Business
Contact Information for Business Card
Name
Title
Mobile number
email address
www.tbkc.com.au
Look and feel
Each slider illustrates characteristics of the customer's brand and the style your logo design should communicate.

```html
<!DOCTYPE html>
<html lang="en">
<head>
<meta charset="utf-8">
<title>Tealbrook Consulting – Business Card</title>
<link href="https://fonts.googleapis.com/css2?family=Roboto:wght@400;500;700&display=swap" rel="stylesheet">
<style>
  :root {
    --brand-blue: #1274be;
    --brand-orange: #f0592a;
    --paper: #ffffff;
    --ink: #1e1e1e;
    --stage: #5c6670;
  }
  * { box-sizing: border-box; margin: 0; padding: 0; }
  html, body { width: 1200px; height: 900px; overflow: hidden; }
  body {
    background: var(--stage);
    font-family: "Roboto", Arial, sans-serif;
    display: flex;
    flex-direction: column;
    align-items: center;
    justify-content: center;
    gap: 60px;
  }
  .card {
    position: relative;
    width: 560px;
    height: 320px;
    border-radius: 18px;
    overflow: hidden;
  }

  /* Back side */
  .card-back {
    background: var(--brand-blue);
    display: flex;
    flex-direction: column;
    align-items: center;
    justify-content: center;
  }
  .card-back .brand-name {
    color: var(--paper);
    font-weight: 700;
    font-size: 44px;
    letter-spacing: 0.5px;
    line-height: 1.1;
    text-align: center;
  }
  .card-back .website {
    position: absolute;
    left: 40px;
    bottom: 34px;
    color: var(--paper);
    font-size: 14px;
  }

  /* Front side */
  .card-front { background: var(--paper); }
  .card-front .backdrop { position: absolute; inset: 0; }
  .card-front .brand-name {
    position: absolute;
    left: 36px;
    top: 34px;
    color: var(--brand-blue);
    font-weight: 700;
    font-size: 30px;
    letter-spacing: 0.3px;
  }
  .contact-list {
    position: absolute;
    left: 36px;
    top: 118px;
    list-style: none;
    display: flex;
    flex-direction: column;
    gap: 9px;
  }
  .contact-item {
    display: flex;
    align-items: center;
    gap: 10px;
    font-size: 13px;
    color: var(--ink);
  }
  .contact-icon {
    width: 20px;
    height: 20px;
    border-radius: 3px;
    background: var(--brand-blue);
    display: flex;
    align-items: center;
    justify-content: center;
  }
  .name-tag {
    position: absolute;
    right: 34px;
    top: 112px;
    text-align: center;
    color: var(--paper);
  }
  .name-tag .person {
    font-size: 24px;
    font-weight: 400;
    letter-spacing: 0.5px;
  }
  .name-tag .role {
    font-size: 10px;
    letter-spacing: 1px;
    margin-top: 2px;
  }
</style>
</head>
<body>

  <section class="card card-front" aria-label="Card front">
    <svg class="backdrop" width="560" height="320" viewBox="0 0 560 320" aria-hidden="true">
      <polygon points="170,320 360,140 560,140 560,320" fill="var(--brand-blue)"/>
      <polygon points="300,92 560,92 560,172 270,172 300,132" fill="var(--brand-orange)"/>
    </svg>

    <div class="brand-name">Tealbrook Consulting</div>

    <ul class="contact-list">
      <li class="contact-item">
        <span class="contact-icon">
          <svg width="12" height="12" viewBox="0 0 24 24" aria-hidden="true"><path fill="#fff" d="M6.6 10.8a15.1 15.1 0 0 0 6.6 6.6l2.2-2.2a1 1 0 0 1 1-.25 11.4 11.4 0 0 0 3.6.57 1 1 0 0 1 1 1V20a1 1 0 0 1-1 1A17 17 0 0 1 3 4a1 1 0 0 1 1-1h3.5a1 1 0 0 1 1 1c0 1.25.2 2.450.57 3.57a1 1 0 0 1-.25 1z"/></svg>
        </span>
        0412 555 018
      </li>
      <li class="contact-item">
        <span class="contact-icon">
          <svg width="12" height="12" viewBox="0 0 24 24" aria-hidden="true"><rect x="2" y="5" width="20" height="14" rx="1" fill="none" stroke="#fff" stroke-width="2"/><path d="M2 6l10 7 10-7" fill="none" stroke="#fff" stroke-width="2"/></svg>
        </span>
        alex@tbkc.com.au
      </li>
      <li class="contact-item">
        <span class="contact-icon">
          <svg width="12" height="12" viewBox="0 0 24 24" aria-hidden="true"><circle cx="12" cy="12" r="9" fill="none" stroke="#fff" stroke-width="2"/><path d="M3 12h18M12 3c3 3 3 15 0 18M12 3c-3 3-3 15 0 18" fill="none" stroke="#fff" stroke-width="1.6"/></svg>
        </span>
        www.tbkc.com.au
      </li>
    </ul>

    <div class="name-tag">
      <div class="person">ALEX MARLOW</div>
      <div class="role">OWNER</div>
    </div>
  </section>

  <section class="card card-back" aria-label="Card back">
    <div class="brand-name">Tealbrook Consulting</div>
    <div class="website">www.tbkc.com.au</div>
  </section>

</body>
</html>
```